Upmarket building and construction company needs signage

Our building company R Brent Construction, needs signage to put up on the side of our vehicle trailers and on site fencing. We are a building company that specialises in residential construction and carpentry .

I will attach our logo and some inspirational pics for site fencing as well as what our trailer looks like .
Other details i would like on the sign are our
( email) rbrentconstruction@mailbox-example.net
(mobile ) 0493 518 264
(website ) rbrentconstruction. example.net

Target Market(s)

Home owners looking for a reliable local builder who produces good quality work. I have attached some inspirational pics.

Industry/Entity Type

Building and Construction

Colors

Designer to choose colors to be used in the design.

Requirements
Must have
• Our logo, contact information
Nice to have
• We would like the design to have elements of being Elegant, Serious, Modern, Professional, Masculine, Conservative and Upmarket.

```html
<!DOCTYPE html>
<html lang="en">
<head>
<meta charset="utf-8">
<title>R Brent Construction – Site Signage</title>
<link rel="stylesheet" href="https://fonts.googleapis.com/css2?family=Jost:wght@300&family=Montserrat:wght@400;500&display=swap">
<style>
  :root {
    --page: #ffffff;
    --slate: #737371;
    --edge: #c8c8c8;
    --ink-light: #ffffff;
  }
  html, body {
    margin: 0;
    padding: 0;
    width: 1200px;
    height: 1200px;
    overflow: hidden;
    background: var(--page);
  }
  .canvas {
    position: relative;
    width: 1200px;
    height: 1200px;
  }
  .sign {
    position: absolute;
    left: 0;
    top: 383px;
    width: 1200px;
    height: 457px;
    box-sizing: border-box;
    border: 1px solid var(--edge);
    background: var(--page);
    overflow: hidden;
  }
  .sign__field {
    position: absolute;
    inset: 0;
    width: 100%;
    height: 100%;
  }
  .brand {
    position: absolute;
    left: 80px;
    top: 160px;
    width: 304px;
    color: var(--slate);
    font-family: "Jost", sans-serif;
    font-weight: 300;
    text-transform: uppercase;
  }
  .brand__name {
    margin: 0;
    font-weight: 300;
    line-height: 1;
  }
  .brand__name-main {
    display: block;
    font-size: 66px;
    letter-spacing: 2px;
  }
  .brand__name-sub {
    display: block;
    margin-top: 14px;
    font-size: 35px;
    letter-spacing: 2.4px;
  }
  .brand__tagline {
    margin: 10px 0 0;
    font-size: 21px;
    letter-spacing: 1.6px;
    line-height: 1;
  }
  .contact {
    position: absolute;
    left: 548px;
    top: 273px;
    display: flex;
    align-items: center;
    color: var(--ink-light);
    font-family: "Montserrat", sans-serif;
  }
  .contact__phone {
    font-size: 41px;
    font-weight: 400;
    letter-spacing: -0.5px;
    line-height: 1;
    padding-right: 11px;
  }
  .contact__divider {
    width: 1px;
    height: 63px;
    background: var(--ink-light);
  }
  .contact__online {
    padding-left: 11px;
    font-size: 15.5px;
    font-weight: 500;
    line-height: 1.3;
  }
</style>
</head>
<body>
  <div class="canvas">
    <section class="sign" aria-label="R Brent Construction signage">
      <svg class="sign__field" viewBox="0 0 1200 457" preserveAspectRatio="none" aria-hidden="true">
        <polygon points="196,457 973,0 1200,0 1200,457" fill="var(--slate)"/>
      </svg>

      <div class="brand">
        <h1 class="brand__name">
          <span class="brand__name-main">R Brent</span>
          <span class="brand__name-sub">Construction</span>
        </h1>
        <p class="brand__tagline">Building and Carpentry</p>
      </div>

      <div class="contact">
        <div class="contact__phone">0493 518 264</div>
        <div class="contact__divider"></div>
        <div class="contact__online">
          <div class="contact__email">rbrentconstruction@mailbox-example.net</div>
          <div class="contact__web">rbrentconstruction. example.net</div>
        </div>
      </div>
    </section>
  </div>
</body>
</html>
```